Brochure for real estate company

We need the brochure in the attachement re-designed in a consistent way with our website. The text and the structure of the text should not be altered, but addidtional design-elements and other stuff can be added. We're looking for a simple and catchy design as in our website (www.kranich-wohnbau.ch). We need design propositions in file formats where we can always change the text ourselves if that is neccessary later on.

Industry/Entity Type

Real Estate

Font styles to use
Sans Serif

Colors
ec2027
f04a50

```html
<!DOCTYPE html>
<html lang="de">
<head>
<meta charset="utf-8">
<title>Dokumentation &amp; Insertion</title>
<link rel="stylesheet" href="https://fonts.googleapis.com/css2?family=Noto+Sans:wght@400;700&family=Rokkitt:wght@400&display=swap">
<style>
  :root {
    --red: #ec2027;
    --red-soft: #f04a50;
    --ground: #dddddd;
    --line: #6f6f6f;
    --ink: #2b2b2b;
    --photo-dark: #121d30;
    --photo-mid: #2a3a55;
  }
  * { margin: 0; padding: 0; box-sizing: border-box; }
  html, body { width: 899px; height: 1200px; overflow: hidden; }
  body {
    background: var(--ground);
    font-family: "Noto Sans", Arial, sans-serif;
    color: var(--ink);
    position: relative;
  }
  .callout {
    position: absolute;
    left: 61px; top: 204px;
    width: 806px; height: 105px;
  }
  .callout svg { position: absolute; inset: 0; }
  .callout-text {
    position: absolute;
    left: 34px; top: 8px;
    font-weight: 700;
    font-size: 18px;
    line-height: 30px;
    color: var(--red);
  }
  .hero-photo {
    position: absolute;
    left: 0; top: 317px;
    width: 899px; height: 485px;
    background: linear-gradient(135deg, var(--photo-mid) 0%, var(--photo-dark) 100%);
  }
  .services {
    position: absolute;
    left: 0; top: 827px;
    width: 899px;
  }
  .services-title {
    font-family: "Rokkitt", Georgia, serif;
    font-weight: 400;
    font-size: 23px;
    color: var(--red);
    margin-left: 86px;
    line-height: 34px;
  }
  .service-list { list-style: none; margin-top: 2px; }
  .service {
    position: relative;
    padding-left: 87px;
    padding-right: 90px;
    font-size: 16.5px;
    line-height: 30px;
    margin-bottom: 30px;
  }
  .service svg {
    position: absolute;
    left: 47px; top: 8px;
  }
  .service strong { font-weight: 700; }
</style>
</head>
<body>
  <div class="callout">
    <svg width="806" height="105" viewBox="0 0 806 105">
      <polyline points="17,1 805,1 805,84 590,84 575,104 575,84 17,84" fill="none" stroke="var(--line)" stroke-width="1.2"/>
      <rect x="0" y="0" width="17" height="85" fill="var(--red)"/>
    </svg>
    <p class="callout-text">Die Basis einer seriösen Vermittlung ist die lückenlose Darstellung.<br>Gemeinsam beginnen wir mit dem ersten Schritt.</p>
  </div>

  <div class="hero-photo" role="img" aria-label="Foto: Hände reichen ein kleines Modellhaus und einen Hausschlüssel"></div>

  <section class="services">
    <h2 class="services-title">Dokumentation &amp; Insertion</h2>
    <ul class="service-list">
      <li class="service">
        <svg width="38" height="16" viewBox="0 0 38 16"><rect x="1" y="4" width="14" height="8" rx="4" fill="none" stroke="var(--red)" stroke-width="2"/><path d="M15 5h10V1l12 7-12 7v-4H15z" fill="var(--red-soft)"/></svg>
        Verkaufsdokumentation: Wir erstellen für Sie ein ansprechendes und<br><strong>bankkonformes</strong> Dossier.
      </li>
      <li class="service">
        <svg width="38" height="16" viewBox="0 0 38 16"><rect x="1" y="4" width="14" height="8" rx="4" fill="none" stroke="var(--red)" stroke-width="2"/><path d="M15 5h10V1l12 7-12 7v-4H15z" fill="var(--red-soft)"/></svg>
        <strong>Insertion:</strong> Wir inserieren für Sie kostenlos und umfassend. Durch intelligenten Einsatz der Verkaufskanäle erscheint Ihr Objekt immer am richtigen Ort.
      </li>
      <li class="service">
        <svg width="38" height="16" viewBox="0 0 38 16"><rect x="1" y="4" width="14" height="8" rx="4" fill="none" stroke="var(--red)" stroke-width="2"/><path d="M15 5h10V1l12 7-12 7v-4H15z" fill="var(--red-soft)"/></svg>
        <strong>Aktualität:</strong> Titel, Texte und Bilder halten wir stets aktuell.
      </li>
    </ul>
  </section>
</body>
</html>
```